Website for boutique digital agency helping high-tech startups accelerate growth.

We need a website design for a relatively young company based in Mauritius called 'LoomTrax'.

We are a professional services firm delivering digital infrastructure for revenue operations (RevOps)*.

Entrepreneurial startups and SMBs in the technology sector work with us to accelerate growth by delivering extraordinary customer experiences across the full customer lifecycle.

We would like a colourful design that utilises the (4) colours of our existing logo design.

The final design should communicate dynamic growth through relentless customer focus.
----------------------------------------------------------
*Revenue Operations (RevOps) is the strategic alignment of sales, marketing and customer success operations to accelerate growth by delivering extraordinary customer experiences across the full customer life cycle.
Updates

Target Market(s)

Entrepreneurial startups and SMBs (Small/Medium Businesses) in the technology sector.

Question: Why the technology sector?

Answer: Because technology entrepreneurs often have a tremendous challenge to effectively communicate to the market and to prospective customers the value and the benefits of their products & services due to the inherent complexity of technological innovation.

LoomTrax is a team of creatively-minded engineers and technologists who have worked with and understand the technologies and innovations our clients are passionate about bringing to market.

Industry/Entity Type

Professional Service

Number of Pages Required

5+ page

Font styles to use
Sans Serif

Requirements
Must have
• Minimalistic designs rich with visual meaning are highly preferred. Mobile responsive designs are also required. Must show how designs render on Desktop, Tablet and Smartphone devices.

Website pages:
1) Homepage: problem statement, target customers, value proposition & benefits
2) Services: 3-4 tiers of services packages with pricing and "how to work with us"
3) Resources: links to all kinds of relevant materials
4) Contact Us: contact form and special project quote form
5) Blog: matrix design with featured images for each post
Nice to have
• Bold, interesting, colourful, inspiring images that visually communicate:
- relentless customer focus
- extraordinary, memorable experiences
- business at the speed of innovation
Should not have
• Any meme or theme that panders to "political correctness".

```html
<!DOCTYPE html>
<html lang="en">
<head>
<meta charset="utf-8">
<title>LoomTrax — Revenue Operations</title>
<link href="https://fonts.googleapis.com/css2?family=Nunito+Sans:wght@300;400;600;700;800&display=swap" rel="stylesheet">
<style>
:root{
  --teal:#0f7a84;
  --teal-dark:#0b5f68;
  --green:#7cb518;
  --orange:#f0841d;
  --ink:#1d1f23;
  --text:#555b63;
  --muted:#8a9097;
  --light:#f3f4f6;
  --footer:#1f2124;
  --white:#ffffff;
}
*{box-sizing:border-box;margin:0;padding:0}
html,body{width:1200px;height:3826px;overflow:hidden}
body{font-family:"Nunito Sans",Arial,sans-serif;color:var(--text);background:var(--white);position:relative}
a{text-decoration:none;color:inherit}
.grad{background:linear-gradient(90deg,var(--green),var(--orange))}

.topbar{height:40px;background:var(--teal);color:#d8eef0;font-size:13px;display:flex;align-items:center;justify-content:space-between;padding:0 32px}
.topbar b{color:#fff;font-weight:700}
.topbar .contacts{display:flex;gap:34px;align-items:center}
.topbar .contacts span{display:flex;align-items:center;gap:8px}

.nav{height:80px;display:flex;align-items:center;justify-content:space-between;padding:0 64px;border-bottom:1px solid #e6e6e6}
.brand{display:flex;align-items:center;gap:10px;font-weight:800;font-size:17px;color:var(--ink)}
.brand .dot{width:26px;height:26px;border-radius:50%;background:var(--teal)}
.menu{display:flex;align-items:center;gap:54px;font-size:13px;color:#444}
.menu .active{color:var(--green)}
.btn-grad{display:inline-flex;align-items:center;justify-content:center;color:#fff;font-weight:700;border-radius:30px}
.menu .btn-grad{width:120px;height:38px;font-size:13px}

.hero{height:480px;position:relative;background:radial-gradient(circle at 25% 30%,#3d8c8f 0%,#1f6d75 35%,#0f5861 70%,#0a4750 100%)}
.hero-title{position:absolute;left:62px;top:170px;font-size:104px;font-weight:800;color:#fff;letter-spacing:-1px;line-height:1}
.hero-copy{position:absolute;left:616px;top:178px;width:500px;color:#fff}
.hero-copy h2{font-weight:300;font-size:28px;margin-bottom:6px}
.hero-copy p{font-size:18px;line-height:29px;font-weight:300}
.btn-line{display:inline-flex;align-items:center;justify-content:center;border:1.5px solid var(--teal);color:var(--teal);border-radius:20px;font-size:12px;width:120px;height:38px}
.hero .btn-line{border-color:#fff;color:#fff;position:absolute;left:616px;top:367px}

.areas{height:360px;background:var(--light);position:relative;text-align:center}
.eyebrow{font-size:13px;color:var(--teal)}
.areas .eyebrow{padding-top:62px}
.area-grid{display:flex;justify-content:space-between;padding:0 48px;margin-top:50px}
.area{width:262px}
.area svg{height:42px;width:42px}
.area h3{font-size:19px;color:var(--ink);font-weight:700;margin:14px 0 14px}
.area p{font-size:12.5px;line-height:19px;color:var(--muted)}
.round-arrow{position:absolute;left:166px;top:332px;width:40px;height:40px;border-radius:50%;background:var(--teal);display:flex;align-items:center;justify-content:center}

.benefits{text-align:center;padding-top:60px}
.benefits h2{font-size:28px;line-height:35px;color:var(--ink);font-weight:700;margin-top:14px}

.feature{position:absolute;left:0;width:1200px;height:360px}
.feature .photo{position:absolute;width:632px;height:360px;top:0}
.feature .copy{position:absolute;width:380px}
.feature h3{font-size:18px;color:var(--ink);font-weight:700;margin-bottom:24px}
.feature p{font-size:13px;line-height:22.5px;text-align:justify;margin-bottom:34px;color:var(--text)}
.f1{top:1185px}.f1 .photo{left:504px;background:linear-gradient(135deg,#c9ccd0,#6d7378 55%,#2e3237)}.f1 .copy{left:64px;top:64px}
.f2{top:1609px}.f2 .photo{left:64px;background:radial-gradient(circle at 50% 48%,#525458 0%,#2b2c2f 30%,#1c1d20 70%)}.f2 .copy{left:760px;top:64px}
.f3{top:2033px}.f3 .photo{left:504px;background:linear-gradient(135deg,#4c5960,#7a8a8c 45%,#2b3a40)}.f3 .copy{left:64px;top:64px}

.quote{position:absolute;top:2456px;left:0;width:1200px;height:400px;background:var(--teal);text-align:center;color:#fff}
.quote .label{font-size:13px;margin-top:62px}
.quote blockquote{font-size:28px;line-height:39px;font-weight:300;color:#cfe8ea;width:820px;margin:22px auto 0}
.person{display:flex;align-items:center;justify-content:center;gap:22px;margin-top:46px;text-align:left}
.avatar{width:80px;height:80px;border-radius:50%;background:linear-gradient(135deg,#d8c3b0,#8d7a6b)}
.person h4{font-size:18px;font-weight:700}
.person p{font-size:12.5px;color:#cfe8ea;line-height:18px}

.insights{position:absolute;top:2921px;left:64px;width:1072px;height:400px}
.card-sub{position:absolute;left:0;top:0;width:336px;height:400px;background:#fff;box-shadow:0 4px 24px rgba(0,0,0,.08);padding:38px 34px}
.card-sub h2{font-size:54px;font-weight:700;color:var(--ink);letter-spacing:-1px}
.card-sub .lead{font-size:18px;margin-top:12px;color:#555}
.card-sub .small{font-size:12.5px;color:var(--muted)}
.field{height:46px;border-radius:24px;background:#f1f2f4;margin-top:26px;padding-left:24px;display:flex;align-items:center;font-size:11px;color:#aaa}
.field+.field{margin-top:16px}
.card-sub .btn-grad{width:128px;height:46px;font-size:13px;margin-top:26px}
.posts{position:absolute;left:400px;top:28px;width:260px}
.post{margin-bottom:24px}
.date{font-size:9px;font-weight:700;color:var(--teal);letter-spacing:.5px}
.post p{font-size:14px;line-height:19px;color:#444;margin-top:4px}
.link-green{font-size:12.5px;color:var(--green)}
.card-feat{position:absolute;left:737px;top:0;width:335px;height:400px;background:#fff;box-shadow:0 4px 24px rgba(0,0,0,.06)}
.card-feat .photo{height:158px;background:linear-gradient(180deg,#1e2a4a,#4a4d6b 60%,#c59a4f)}
.card-feat .body{padding:22px 30px}
.card-feat h4{font-size:18px;line-height:23px;color:var(--ink);font-weight:700;margin:6px 0 14px}
.card-feat .body p{font-size:11.5px;line-height:17px;color:var(--muted);margin-bottom:30px}

.footer{position:absolute;top:3386px;left:0;width:1200px;height:440px;background:var(--footer);color:#aab0b6}
.footer h2{position:absolute;left:64px;top:62px;font-size:28px;line-height:35px;color:#fff;font-weight:700}
.footer .intro{position:absolute;left:64px;top:148px;width:310px;font-size:12.5px;line-height:19px}
.footer .btn-grad{position:absolute;left:64px;top:250px;width:144px;height:38px;font-size:12.5px}
.footer h3{position:absolute;left:616px;top:86px;font-size:18px;color:#fff;font-weight:700}
.footer .addr{position:absolute;left:616px;top:142px;font-size:13px;line-height:19px;color:#c9cdd1}
.footer .call{position:absolute;left:800px;top:142px}
.footer .call strong{display:block;font-size:19px;color:#fff;font-weight:400}
.footer .call span{font-size:13px}
.social{position:absolute;left:616px;top:250px;display:flex;gap:12px}
.social span{width:38px;height:38px;border-radius:50%;border:1.5px solid #888d92;display:block}
.footnav{position:absolute;left:64px;top:384px;font-size:12.5px;display:flex;gap:14px}
.copyright{position:absolute;left:616px;top:384px;font-size:12.5px}
.footbrand{position:absolute;left:1060px;top:376px;font-size:18px;font-weight:800;color:#5b5f64}
</style>
</head>
<body>

<div class="topbar">
  <div><b>RevOps:</b> We call this Revenue Operations.</div>
  <div class="contacts">
    <span><svg width="16" height="16" viewBox="0 0 16 16"><circle cx="8" cy="8" r="8" fill="#2e9aa3"/><path d="M5.5 4.5l1.5 1.6-.8 1c.5 1 1.2 1.7 2.2 2.2l1-.8 1.6 1.5-.8 1.3c-2.8-.4-5.1-2.7-5.5-5.5z" fill="#fff"/></svg>+1 555 018 2460</span>
    <span><svg width="16" height="16" viewBox="0 0 16 16"><circle cx="8" cy="8" r="8" fill="#2e9aa3"/><rect x="4.5" y="5.5" width="7" height="5" fill="none" stroke="#fff"/><path d="M4.5 5.5l3.5 3 3.5-3" fill="none" stroke="#fff"/></svg>hello@loomtrax.io</span>
  </div>
</div>

<header class="nav">
  <div class="brand"><span class="dot"></span>loomtrax.io</div>
  <nav class="menu">
    <a class="active">Home</a><a>About</a><a>Services</a><a>Resources</a><a>Blog</a>
    <a class="btn-grad grad">Contact</a>
  </nav>
</header>

<section class="hero" role="img" aria-label="Hand reaching toward floating translucent teal cubes">
  <div class="hero-title">loomtrax</div>
  <div class="hero-copy">
    <h2>Technology for Growth &nbsp;–</h2>
    <p>Technology entrepreneurs often have a tremendous challenge due to the inherent complexity of technological innovation.</p>
  </div>
  <a class="btn-line">Learn More</a>
</section>

<section class="areas">
  <p class="eyebrow">RevOps has four areas of responsibility:</p>
  <div class="area-grid">
    <div class="area">
      <svg viewBox="0 0 42 42" fill="none" stroke-width="2"><circle cx="21" cy="11" r="5" stroke="#7cb518"/><circle cx="11" cy="29" r="5" stroke="#f0841d"/><circle cx="31" cy="29" r="5" stroke="#7cb518"/><path d="M21 3v3M21 16v3M13 11h3M26 11h3M11 21v3M11 34v3M3 29h3M16 29h3M31 21v3M31 34v3M23 29h3M36 29h3" stroke="#b49a1c"/></svg>
      <h3>Operations</h3>
      <p>Ut enim ad minim veniam, quis nostrud exercitation ullamco laboris nisi ut aliquip ex ea commodo</p>
    </div>
    <div class="area">
      <svg viewBox="0 0 42 42" fill="none" stroke-width="2"><circle cx="14" cy="14" r="6" stroke="#f0841d"/><circle cx="28" cy="14" r="6" stroke="#7cb518"/><path d="M3 34c0-7 5-11 11-11s11 4 11 11M17 34c0-7 5-11 11-11s11 4 11 11" stroke="#b49a1c"/></svg>
      <h3>Enablement</h3>
      <p>Ut enim ad minim veniam, quis nostrud exercitation ullamco laboris nisi ut aliquip ex ea commodo</p>
    </div>
    <div class="area">
      <svg viewBox="0 0 42 42" fill="none" stroke-width="2"><path d="M21 4a11 11 0 0 0-6 20v5h12v-5A11 11 0 0 0 21 4z" stroke="#7cb518"/><path d="M16 33h10M18 37h6" stroke="#f0841d"/></svg>
      <h3>Insights</h3>
      <p>Ut enim ad minim veniam, quis nostrud exercitation ullamco laboris nisi ut aliquip ex ea commodo</p>
    </div>
    <div class="area">
      <svg viewBox="0 0 42 42" fill="none" stroke-width="2"><path d="M6 36l18-18M26 6a8 8 0 0 0-2 12l4 4a8 8 0 0 0 12-2l-5-1-2-4 3-4z" stroke="#7cb518"/><path d="M8 6l4 1 22 22 2 5-5-2L9 10z" stroke="#f0841d"/></svg>
      <h3>Tools</h3>
      <p>Ut enim ad minim veniam, quis nostrud exercitation ullamco laboris nisi ut aliquip ex ea commodo</p>
    </div>
  </div>
  <a class="round-arrow"><svg width="16" height="16" viewBox="0 0 16 16" fill="none" stroke="#fff" stroke-width="1.6"><path d="M2 8h11M9 4l4 4-4 4"/></svg></a>
</section>

<section class="benefits">
  <p class="eyebrow">Holistic approach has three key benefits:</p>
  <h2>RevOps has one job – to drive growth through operational<br>efficiency across the customer lifecycle.</h2>
</section>

<section class="feature f1">
  <div class="copy">
    <h3>RevOps aligns everyone</h3>
    <p>Nemo enim ipsam voluptatem quia voluptas sit aspernatur aut odit aut fugit, sed quia consequuntur magni dolores eos qui ratione voluptatem sequi nesciunt. Neque porro quisquam est, qui dolorem ipsum quia dolor sit amet, consectetur, adipisci velit.</p>
    <a class="btn-line">Learn More</a>
  </div>
  <div class="photo" role="img" aria-label="Close-up of interlocking metal gears"></div>
</section>

<section class="feature f2">
  <div class="photo" role="img" aria-label="Camera lens seen from above on a dark surface"></div>
  <div class="copy">
    <h3>RevOps creates focus</h3>
    <p>Nemo enim ipsam voluptatem quia voluptas sit aspernatur aut odit aut fugit, sed quia consequuntur magni dolores eos qui ratione voluptatem sequi nesciunt. Neque porro quisquam est, qui dolorem ipsum quia dolor sit amet, consectetur, adipisci velit.</p>
    <a class="btn-line">Learn More</a>
  </div>
</section>

<section class="feature f3">
  <div class="copy">
    <h3>RevOps simplifies everything</h3>
    <p>Nemo enim ipsam voluptatem quia voluptas sit aspernatur aut odit aut fugit, sed quia consequuntur magni dolores eos qui ratione voluptatem sequi nesciunt. Neque porro quisquam est, qui dolorem ipsum quia dolor sit amet, consectetur, adipisci velit.</p>
    <a class="btn-line">Learn More</a>
  </div>
  <div class="photo" role="img" aria-label="Robotic grippers solving a colour cube puzzle"></div>
</section>

<section class="quote">
  <p class="label">Who leads RevOps?</p>
  <blockquote>“ The integration between Marketing, Sales, and Customer Success is critical – the CRO’s role is to drive alignment between these teams.”</blockquote>
  <div class="person">
    <div class="avatar" role="img" aria-label="Portrait photo of the quoted executive"></div>
    <div>
      <h4>Daniel Hartwell</h4>
      <p>Previously Chief Revenue Officer<br>@ Funnelworks</p>
    </div>
  </div>
</section>

<section class="insights">
  <div class="card-sub">
    <h2>Insights.</h2>
    <p class="lead">Keep up to date —</p>
    <p class="small">get updates with latest topics.</p>
    <div class="field">Your Name</div>
    <div class="field">Email</div>
    <a class="btn-grad grad">Subscribe</a>
  </div>
  <div class="posts">
    <div class="post"><span class="date">MAR 21, 2014</span><p>Sed ut perspiciatis unde omnis iste natus error sit</p></div>
    <div class="post"><span class="date">MAR 21, 2014</span><p>Investment update, fourth quarter 2016</p></div>
    <div class="post"><span class="date">MAR 21, 2014</span><p>Sed ut perspiciatis unde omnis iste natus error sit</p></div>
    <div class="post"><span class="date">MAR 21, 2014</span><p>9 resources to get you prepared for tax season</p></div>
    <a class="link-green">Explore All</a>
  </div>
  <div class="card-feat">
    <div class="photo" role="img" aria-label="Night aerial view of city skyscrapers"></div>
    <div class="body">
      <span class="date">MAR 21, 2014</span>
      <h4>9 resources to get you prepared for tax season</h4>
      <p>Sed ut perspiciatis unde omnis iste natus error sit voluptatem accusantium doloremque laudantium</p>
      <a class="link-green">Read More</a>
    </div>
  </div>
</section>

<footer class="footer">
  <h2>Getting started<br>with RevOps</h2>
  <p class="intro">It is a long established fact that a reader will be distracted by the readable content of a page when looking at its layout.</p>
  <a class="btn-grad grad">Let’s help you!</a>
  <h3>Contact us</h3>
  <p class="addr">14 Harbour Row<br>Suite 3,<br>Port Lorel 20417,<br>USA</p>
  <div class="call"><strong>Call Us. +1 555 018 2460</strong><span>e. hello@loomtrax.io</span></div>
  <div class="social" aria-label="Social links"><span></span><span></span><span></span><span></span></div>
  <nav class="footnav"><a>About</a>·<a>Services</a>·<a>Resources</a>·<a>Blog</a>·<a>Contact</a></nav>
  <p class="copyright">© 2020 loomtrax.io. All Rights Reserved.</p>
  <div class="footbrand">LoomTrax</div>
</footer>

</body>
</html>
```